Business Card Design for Clinical Therapist

I will operate in 3 product areas as follows...
I will operate as Psychotherapist providing an opportunity for individuals to stop, reflect, heal, and gain hope in a safe and professional atmosphere. My task as a Licensed Mental Health Social Worker is to work “along-side” the client to help guide them toward answers they may seek. I believe that all difficulties contain a small seed of opportunity within them and I can support the individual in clarifying issues while resolving obstacles that may get in the way.
1-Therapy
Treatment Issues may include:
• Addiction
• Bipolar Disorder
• Adolescent or Adult
• Coping Skills
• Dual Diagnosis
• Family Conflict
• Sleep or Insomnia
• Substance Abuse
• Anger Management
• Career Counseling
• Drug Abuse
• Emotional Disturbance
• Grief
• Self Esteem
• Trauma and PTSD
Treatment Orientation may include but not be limited to:
• CBT
• EMDR
• Person-Centered
• Mindfulness based (MBCT)
• Motivational Interviewing

2-Other Substance Abuse Services
SAP Assessments
Employees performing safety-sensitive duties under US Bureau of Roadway Affairs rules must have an evaluation by a qualified Substance Abuse Professional when they are in violation of BRA rules (for a positive test or a refusal to test). I am a BRA qualified SAP and can perform these evaluations, which involve specialized assessment and compliance reports, as well as a return to work assessment.

3-DUI/OVUII Assessments
Substance abuse assessment reports-State level assessments targeted for the court system.

Somehow I would like the final design to acknowledge the three areas of services, or two being therapy for mental health services and combining SAP/OVUII assessment reporting for Substance abuse)

Industry/Entity Type

Mental Health

Contact Information for Business Card

Brightwell Harbor LLC,
Desmond Farrowby LCSW
Clinical Therapist
2087 West Palmer Avenue, STE 412
Honolulu, HI 96720
808.555.0193
brightwellharborllc.example

Colors

Designer to choose colors to be used in the design.

```html
<!DOCTYPE html>
<html lang="en">
<head>
<meta charset="utf-8">
<title>Brightwell Harbor LLC — Business Card</title>
<link rel="stylesheet" href="https://fonts.googleapis.com/css2?family=Didact+Gothic&display=swap">
<style>
  :root {
    --page: #e9e7e3;
    --charcoal: #4a4a4b;
    --teal: #2cc3b9;
    --ink-light: #ffffff;
    --ink-teal: #3f6f6b;
    --brand-dot: #f39a2b;
  }
  * { box-sizing: border-box; margin: 0; padding: 0; }
  html, body {
    width: 1200px; height: 903px; overflow: hidden;
    background: var(--page);
    font-family: "Didact Gothic", "Century Gothic", sans-serif;
  }
  .card {
    position: absolute; left: 100px; top: 166px;
    width: 1000px; height: 571px;
    border-radius: 40px; overflow: hidden;
    box-shadow: 0 6px 22px rgba(0,0,0,.18);
  }
  .card-bg { position: absolute; inset: 0; }
  .therapy, .orientation {
    position: absolute; top: 28px;
    color: var(--ink-light); font-size: 22px; line-height: 26.5px;
  }
  .therapy { left: 30px; }
  .orientation { left: 310px; }
  .therapy h2 { font-size: 22px; font-weight: 400; letter-spacing: .3px; text-shadow: 0 0 .6px #fff; }
  .bullets { list-style: none; }
  .bullets li { padding-left: 24px; position: relative; white-space: nowrap; }
  .bullets li::before {
    content: ""; position: absolute; left: 4px; top: 10px;
    width: 7px; height: 7px; border-radius: 50%; background: var(--ink-light);
  }
  .services {
    position: absolute; left: 662px; top: 26px; width: 314px;
    color: var(--ink-teal); font-size: 14.5px; line-height: 19px;
  }
  .services h3 { font-size: 14.5px; font-weight: 400; margin-bottom: 22px; }
  .services h4 { font-size: 14.5px; font-weight: 400; text-shadow: 0 0 .5px var(--ink-teal); }
  .services p { margin-bottom: 34px; }
  .brand {
    position: absolute; right: 30px; bottom: 122px;
    display: flex; align-items: center; gap: 10px;
  }
  .brand-dot { width: 24px; height: 24px; border-radius: 50%; background: var(--brand-dot); }
  .brand-name {
    font-size: 22px; color: var(--ink-teal); letter-spacing: .3px;
    text-transform: uppercase; white-space: nowrap;
  }
</style>
</head>
<body>
  <article class="card">
    <svg class="card-bg" width="1000" height="571" viewBox="0 0 1000 571" aria-hidden="true">
      <rect width="1000" height="571" fill="var(--teal)"/>
      <polygon points="0,0 605,0 650,571 0,571" fill="var(--charcoal)"/>
    </svg>

    <section class="therapy">
      <h2>Therapy</h2>
      <p>Treatment issues<br>may include:</p>
      <ul class="bullets">
        <li>Addiction</li>
        <li>Bipolar Disorder</li>
        <li>Adolescent and Adult</li>
        <li>Coping Skills</li>
        <li>Dual Diagnosis</li>
        <li>Family Conflict</li>
        <li>Sleep or Insomnia</li>
        <li>Substance Abuse</li>
        <li>Anger Management</li>
        <li>Career Counseling</li>
        <li>Drug Abuse</li>
        <li>Emotional Disturbance</li>
        <li>Grief</li>
        <li>Self Esteem</li>
        <li>Trauma and PTSD</li>
      </ul>
    </section>

    <section class="orientation">
      <p>Treatment Orientation<br>may include<br>but not be limited to:</p>
      <ul class="bullets">
        <li>CBT</li>
        <li>EMDR</li>
        <li>Person-Centered</li>
        <li>Mindfulness based (MBCT)</li>
        <li>Motivational Interviewing</li>
      </ul>
    </section>

    <section class="services">
      <h3>Other Substance Abuse Services :</h3>
      <h4>SAP services</h4>
      <p>-Employees performing safety-sensitive duties under US Bureau of Roadway Affairs rules must have an evaluation by a qualified Substance Abuse Professional when they are in violation of BRA rules (for a positive test or a refusal to test).</p>
      <h4>DUI/OVUII</h4>
      <p>-Substance abuse assessment reports<br>-State level assessments targeted for the court system.</p>
    </section>

    <div class="brand">
      <span class="brand-dot" aria-hidden="true"></span>
      <span class="brand-name">Brightwell Harbor LLC</span>
    </div>
  </article>
</body>
</html>
```